Modernes Geschäftspapiere für Beratung zum Thema digitale Kommunikation & Zusammenarbeit
Zielgruppe
Beratung zum Thema digitale Kommunikation und Zusammenarbeit (z.B. Videoberatung, Chats, etc.).
Zielgruppe sind mittelständische und große Unternehmen sowie Behörden, Banken und Versicherungen.
Aufgabenstellung
Die Firmenfarbe ist HEX #6CC24A
Das Design sollte modern sein und nicht zu verspielt.
Das Design muss Platz bieten für alle relevanten Angaben einer GmbH (Adresse, Geschäftsführer, Kontaktmöglichkeiten, Registergericht und -nummer, Steuernummer und Bankverbindung)

```html
<!DOCTYPE html>
<html lang="de">
<head>
<meta charset="utf-8">
<title>Klarwerk Haus GmbH – Briefbogen</title>
<link href="https://fonts.googleapis.com/css2?family=Open+Sans:wght@300;400;600;700&display=swap" rel="stylesheet">
<style>
  :root {
    --brand-green: #6cc24a;
    --pale-green: #eef6ea;
    --ink: #333333;
    --ink-soft: #555555;
    --muted: #8a8a8a;
    --paper: #ffffff;
    --backdrop: #e9e9ea;
  }
  * { box-sizing: border-box; margin: 0; padding: 0; }
  html, body {
    width: 1200px; height: 1010px; overflow: hidden;
    background: var(--backdrop);
    font-family: "Open Sans", Arial, sans-serif;
    color: var(--ink);
  }
  .letterhead {
    position: absolute; left: 260px; top: 24px;
    width: 680px; height: 962px;
    background: var(--paper);
    box-shadow: 0 2px 10px rgba(0,0,0,.12);
    overflow: hidden;
  }
  .backdrop-pattern {
    position: absolute; left: 150px; top: 300px;
    width: 360px; height: 460px;
    border-radius: 40px;
    background: linear-gradient(160deg, var(--pale-green), #f4f9f1 70%, rgba(244,249,241,0));
  }
  .sender-line {
    position: absolute; left: 300px; top: 62px;
    font-size: 8.5px; font-weight: 300; color: var(--muted);
  }
  .letter-body {
    position: absolute; left: 70px; top: 130px; width: 420px;
    font-size: 11px; line-height: 1.45; color: var(--ink-soft);
  }
  .letter-body .salutation { font-weight: 600; margin-bottom: 20px; }
  .letter-body p { margin-bottom: 12px; text-align: justify; }
  .closing { margin-top: 22px; font-weight: 600; }
  .signature-area {
    width: 110px; height: 44px; margin-top: 8px;
    background: linear-gradient(90deg, #f3f3f3, #fafafa);
    border-radius: 4px;
  }
  .wordmark {
    position: absolute; left: 560px; top: 640px;
    transform-origin: 0 0; transform: rotate(-90deg);
    font-size: 88px; font-weight: 400; letter-spacing: -3px;
    line-height: 1; color: var(--ink); white-space: nowrap;
  }
  .contact-block {
    position: absolute; left: 440px; top: 660px; width: 210px;
    font-size: 10px; line-height: 1.45; color: var(--muted);
  }
  .contact-block .claim { font-weight: 700; color: var(--ink-soft); margin-bottom: 14px; }
  .contact-block .company { font-weight: 700; color: var(--ink-soft); }
  .contact-list { list-style: none; margin-top: 14px; }
  .contact-list li { display: flex; align-items: center; gap: 7px; height: 15px; }
  .contact-list svg { width: 11px; height: 11px; flex: none; }
  .legal-footer {
    position: absolute; left: 40px; bottom: 36px;
    display: flex; gap: 16px; align-items: center;
    font-size: 9px; line-height: 1.5; color: var(--muted);
  }
  .legal-footer .divider { width: 1px; height: 22px; background: #b5b5b5; transform: skewX(-20deg); }
</style>
</head>
<body>
<main class="letterhead">
  <div class="backdrop-pattern" role="img" aria-label="Zarte hellgrüne Flächen aus abgerundeten Formen als Hintergrundmuster"></div>

  <div class="sender-line">Klarwerk Haus GmbH | Talgasse 14 | 90521 Nordhain</div>

  <section class="letter-body">
    <div class="salutation">Sehr geehrter Herr Mustermann,</div>
    <p>Lorem ipsum dolor sit amet, consectetuer adipiscing elit, sed diam nonummy nibh euismod tincidunt ut laoreet dolore magna aliquam erat volutpat. Ut wisi enim ad minim veniam, quis nostrud exerci tation ullamcorper suscipit lobortis nisl ut aliquip ex ea commodo consequat. Duis autem vel eum iriure dolor in hendrerit in vulputate velit esse molestie consequat, vel illum dolore eu feugiat nulla facilisis at vero eros et accumsan et iusto odio dignissim qui blandit praesent luptatum zzril delenit augue duis dolore te feugait nulla facilisi.</p>
    <p>Lorem ipsum dolor sit amet, consectetuer adipiscing elit, sed diam nonummy nibh euismod tincidunt ut laoreet dolore magna aliquam erat volutpat. Ut wisi enim ad minim veniam, quis nostrud exerci tation ullamcorper suscipit lobortis nisl ut aliquip ex ea commodo consequat. Duis autem vel eum iriure dolor in hendrerit in vulputate velit esse molestie consequat, vel illum dolore eu feugiat nulla facilisis at vero eros et accumsan et iusto odio dignissim qui blandit praesent luptatum zzril delenit augue duis dolore te feugait nulla facilisi.</p>
    <p>Lorem ipsum dolor sit amet, cons ectetuer adipiscing elit, sed diam nonummy nibh euismod tincidunt ut laoreet dolore magna aliquam erat volutpat. Ut wisi enim ad minim veniam, quis nostrud exerci tation ullamcorper suscipit lobortis nisl ut aliquip ex ea commodo consequat.</p>
    <div class="closing">Mit freundlichen Grüßen</div>
    <div class="signature-area" role="img" aria-label="Handschriftliche Unterschrift"></div>
  </section>

  <div class="wordmark">KlarwerkHaus</div>

  <address class="contact-block" style="font-style:normal">
    <div class="claim">Beratung zum Thema<br>digitale Kommunikation<br>und Zusammenarbeit.</div>
    <div class="company">Klarwerk Haus GmbH</div>
    <div>Lena Obermaier</div>
    <div>Talgasse 14</div>
    <div>90521 Nordhain</div>
    <ul class="contact-list">
      <li><svg viewBox="0 0 12 12"><path d="M3 1l2 2.5-1.2 1.3a6 6 0 0 0 3.4 3.4L8.5 7 11 9l-1.3 2C5.5 11 1 6.5 1 2.3z" fill="var(--brand-green)"/></svg>0911 - 480 12 30 1</li>
      <li><svg viewBox="0 0 12 12"><rect x="1" y="4" width="10" height="6" rx="1" fill="none" stroke="var(--brand-green)" stroke-width="1.3"/><rect x="3" y="1" width="6" height="3" fill="var(--brand-green)"/></svg>0911 - 480 12 30 2</li>
      <li><svg viewBox="0 0 12 12"><rect x="3" y="0.8" width="6" height="10.4" rx="1" fill="none" stroke="var(--brand-green)" stroke-width="1.3"/></svg>0170 - 555 31 47</li>
      <li><svg viewBox="0 0 12 12"><rect x="1" y="2.5" width="10" height="7" fill="none" stroke="var(--brand-green)" stroke-width="1.3"/><path d="M1 2.5l5 4 5-4" fill="none" stroke="var(--brand-green)" stroke-width="1.3"/></svg>info@klarwerkhaus.com</li>
      <li><svg viewBox="0 0 12 12"><circle cx="6" cy="6" r="5" fill="none" stroke="var(--brand-green)" stroke-width="1.3"/><path d="M1 6h10M6 1v10" stroke="var(--brand-green)" stroke-width="1"/></svg>www.klarwerkhaus.com</li>
      <li><svg viewBox="0 0 12 12"><circle cx="6" cy="6" r="5" fill="none" stroke="var(--brand-green)" stroke-width="1.3"/><path d="M4.5 4.6a1.5 1.5 0 1 1 2 1.4L6 6.6v1" fill="none" stroke="var(--brand-green)" stroke-width="1.2"/><circle cx="6" cy="9" r=".7" fill="var(--brand-green)"/></svg>support.klarwerkhaus.de</li>
    </ul>
  </address>

  <footer class="legal-footer">
    <div>Handelsregister<br>AG Musterstadt</div>
    <span class="divider"></span>
    <div>HRB 123456<br>USt.-IdNr. DE47110233</div>
    <span class="divider"></span>
    <div>Rheintal Bank<br>IBAN: DE 12 3456 7890 1234 5678 9</div>
  </footer>
</main>
</body>
</html>
```